PowerPoint template for Law Firm

We Need a PowerPoint Template for a Law Firm in Switzerland. We are primarly consult in business law. We Need a template for PowerPoint to Show Information to our Clients (inheritence law, corporate law, legal structures etc.) The design should be contemporary, simple and clear. It should be in harmony with our website: www.tannquist.com Style: professional, structured and clearly arranged. Colors: Blue (R: 1, G: 61: B: 105), white. Font: Calibri Ratio: 16: 9 Esamples attached

```html
<!DOCTYPE html>
<html lang="de">
<head>
<meta charset="utf-8">
<title>Tannquist Legal – PowerPoint Vorlage</title>
<link href="https://fonts.googleapis.com/css2?family=Carlito:wght@400;700&display=swap" rel="stylesheet">
<style>
  :root{
    --canvas:#FBAE3C;
    --navy:#013D69;
    --mid:#3C7FAD;
    --light:#7FBFE0;
    --pale:#BBDFEE;
    --panel:#F2F2F2;
    --grey:#E6E6E6;
    --chart-bg:#8CA0AC;
    --white:#FFFFFF;
  }
  html,body{margin:0;padding:0;overflow:hidden;}
  body{width:1200px;height:1081px;background:var(--canvas);position:relative;font-family:"Carlito","Calibri",sans-serif;}
  .slide{position:absolute;width:356px;height:216px;overflow:hidden;background:var(--white);}
  .slide svg{display:block;width:100%;height:100%;}
  .slide text{font-family:"Carlito","Calibri",sans-serif;}
  .title-slide{left:423px;top:67px;}
  .s1{left:48px;top:337px}.s2{left:423px;top:337px}.s3{left:794px;top:337px}
  .s4{left:48px;top:572px}.s5{left:423px;top:572px}.s6{left:794px;top:572px}
  .s7{left:48px;top:798px}.s8{left:423px;top:798px}.s9{left:794px;top:798px}
  .h{font-weight:700;font-size:26px;fill:var(--navy);}
  .h-white{font-weight:700;font-size:26px;fill:var(--white);}
  .sub{font-weight:700;font-size:12.5px;fill:var(--navy);}
  .sub-white{font-weight:700;font-size:12.5px;fill:var(--white);}
  .brand{font-size:9px;fill:var(--navy);}
  .brand-white{font-size:9px;fill:var(--white);}
  .sym{font-size:16px;fill:var(--navy);}
</style>
</head>
<body>

<!-- Title slide -->
<div class="slide title-slide">
  <svg viewBox="0 0 600 364">
    <defs>
      <radialGradient id="titleGlow" cx="0.5" cy="0.35" r="0.7">
        <stop offset="0" stop-color="#2A5E8C"/>
        <stop offset="1" stop-color="#0E426F"/>
      </radialGradient>
    </defs>
    <rect width="600" height="364" fill="url(#titleGlow)" role="img" aria-label="Hintergrundfoto: Beratungsgespräch in einem hellen Büro, blau eingefärbt"/>
    <text x="300" y="45" text-anchor="middle" font-size="18" fill="#fff">Tannquist Legal</text>
    <text x="300" y="195" text-anchor="middle" font-size="36" font-weight="700" fill="#fff">Ehe- und Erbschaftsberatung</text>
    <text x="300" y="255" text-anchor="middle" font-size="14" font-weight="700" fill="#fff">Für Ehegatten XY</text>
    <text x="300" y="293" text-anchor="middle" font-size="14" font-weight="700" fill="#fff">28.12.2019</text>
    <text x="300" y="313" text-anchor="middle" font-size="14" font-weight="700" fill="#fff">Martin Brenner</text>
  </svg>
</div>

<!-- Gesetzliche Regelung 1 -->
<div class="slide s1">
  <svg viewBox="0 0 600 364">
    <polygon points="0,0 390,0 0,190" fill="var(--navy)"/>
    <polygon points="600,200 600,364 225,364" fill="var(--navy)"/>
    <rect x="56" y="38" width="493" height="296" fill="#000" opacity="0.12"/>
    <rect x="53" y="34" width="493" height="296" fill="var(--panel)"/>
    <text x="75" y="72" class="h">Gesetzliche Regelung</text>
    <text x="75" y="119" class="sub">1. Güterrechtliche Auseinandersetzung</text>
    <text x="88" y="136" class="sub">Errungenschaftsbeteiligung (ordentlicher Güterstand)</text>
    <text x="88" y="171" class="sub">Beispiel Todesfall Ehemann:</text>
    <rect x="83" y="218" width="81" height="33" fill="var(--navy)"/>
    <rect x="164" y="218" width="196" height="33" fill="var(--mid)"/>
    <rect x="360" y="218" width="80" height="33" fill="var(--light)"/>
    <rect x="83" y="265" width="169" height="33" fill="var(--pale)"/>
    <line x1="262" y1="210" x2="262" y2="322" stroke="#333" stroke-width="1" stroke-dasharray="3 3"/>
    <text x="583" y="358" text-anchor="end" class="brand-white">Tannquist Legal</text>
  </svg>
</div>

<!-- Gesetzliche Regelung 2 -->
<div class="slide s2">
  <svg viewBox="0 0 600 364">
    <rect width="600" height="157" fill="var(--navy)"/>
    <rect y="163" width="600" height="3" fill="var(--navy)"/>
    <text x="76" y="60" class="h-white">Gesetzliche Regelung</text>
    <text x="85" y="93" class="sub-white">2. Erbrechtliche Auseinandersetzung</text>
    <text x="85" y="127" class="sub-white">Beispiel Todesfall Ehemann:</text>
    <text x="88" y="235" class="sym">♂</text>
    <rect x="85" y="250" width="101" height="33" fill="var(--navy)"/>
    <polygon points="214,258 277,258 277,244 300,266 277,288 277,274 214,274" fill="var(--mid)"/>
    <path d="M405 204 A58 58 0 0 0 405 320 Z" fill="var(--mid)"/>
    <path d="M409 204 A58 58 0 0 1 409 320 Z" fill="var(--light)"/>
    <text x="583" y="358" text-anchor="end" class="brand">Tannquist Legal</text>
  </svg>
</div>

<!-- Ehevertrag -->
<div class="slide s3">
  <svg viewBox="0 0 600 364">
    <rect width="103" height="364" fill="var(--navy)"/>
    <rect x="78" y="68" width="490" height="261" fill="#000" opacity="0.12"/>
    <rect x="75" y="64" width="490" height="261" fill="var(--panel)"/>
    <text x="135" y="45" class="h">Ehevertrag</text>
    <text x="140" y="93" class="sub">1. Güterrechtliche Auseinandersetzung</text>
    <text x="153" y="110" class="sub">Errungenschaftsbeteiligung (Vorschlagszuweisung mit Ehevertrag)</text>
    <text x="153" y="127" class="sub">nur möglich gegenüber gemeinsamen Nachkommen</text>
    <text x="140" y="162" class="sub">Beispiel Todesfall Ehemann:</text>
    <text x="137" y="190" class="sym">♂</text>
    <text x="480" y="190" class="sym">♀</text>
    <rect x="135" y="204" width="82" height="32" fill="var(--navy)"/>
    <rect x="217" y="204" width="194" height="32" fill="var(--mid)"/>
    <rect x="411" y="204" width="81" height="32" fill="var(--light)"/>
    <path d="M138 240 V246 H209 V240 M173 246 V251" fill="none" stroke="#333" stroke-width="1"/>
    <rect x="135" y="264" width="82" height="32" fill="var(--pale)"/>
    <line x1="217" y1="180" x2="217" y2="315" stroke="#333" stroke-width="1" stroke-dasharray="3 3"/>
    <text x="583" y="358" text-anchor="end" class="brand">Tannquist Legal</text>
  </svg>
</div>

<!-- Erbvertrag -->
<div class="slide s4">
  <svg viewBox="0 0 600 364">
    <rect x="482" width="118" height="364" fill="var(--navy)"/>
    <rect x="26" y="68" width="489" height="261" fill="#000" opacity="0.12"/>
    <rect x="23" y="64" width="489" height="261" fill="var(--panel)"/>
    <text x="82" y="45" class="h">Erbvertrag</text>
    <text x="72" y="93" class="sub">2. Erbrechtliche Auseinandersetzung</text>
    <text x="72" y="144" class="sub">Beispiel Todesfall Ehemann:</text>
    <text x="73" y="223" class="sym">♂</text>
    <rect x="68" y="238" width="101" height="34" fill="var(--navy)"/>
    <polygon points="197,246 280,246 280,232 302,255 280,278 280,264 197,264" fill="var(--mid)"/>
    <path d="M405 250 L405 196 A54 54 0 0 1 440 291 Z" fill="var(--navy)"/>
    <path d="M405 250 L440 291 A54 54 0 0 1 405 304 Z" fill="var(--mid)"/>
    <path d="M405 250 L405 304 A54 54 0 0 1 405 196 Z" fill="var(--light)"/>
    <text x="583" y="358" text-anchor="end" class="brand-white">Tannquist Legal</text>
  </svg>
</div>

<!-- Erbverzichtsvertrag (leer) -->
<div class="slide s5">
  <svg viewBox="0 0 600 364">
    <rect width="600" height="364" fill="var(--grey)"/>
    <polygon points="0,130 600,290 600,364 0,364" fill="var(--navy)"/>
    <rect x="48" y="32" width="500" height="301" fill="var(--white)"/>
    <text x="98" y="62" class="h">Erbverzichtsvertrag</text>
    <text x="583" y="358" text-anchor="end" class="brand-white">Tannquist Legal</text>
  </svg>
</div>

<!-- Erbverzichtsvertrag (Ausschnitt) -->
<div class="slide s6">
  <svg viewBox="0 0 600 364">
    <polygon points="0,210 430,0 600,0 600,200 270,364 0,364" fill="var(--navy)"/>
    <text x="82" y="45" class="h">Erbverzichtsvertrag</text>
    <rect x="56" y="63" width="482" height="268" fill="#DADADA"/>
    <rect x="62" y="68" width="470" height="258" fill="#F7F7F7" role="img" aria-label="Eingefügter Bildschirmausschnitt: Grafik zu gesetzlichen und freien Erbquoten"/>
    <line x1="410" y1="338" x2="600" y2="338" stroke="var(--navy)" stroke-width="2"/>
    <text x="592" y="358" text-anchor="end" class="brand">Tannquist Legal</text>
  </svg>
</div>

<!-- Erbverzichtsvertrag (Grafik) -->
<div class="slide s7">
  <svg viewBox="0 0 600 364">
    <rect width="600" height="64" fill="var(--navy)"/>
    <rect width="60" height="364" fill="var(--navy)"/>
    <text x="95" y="40" class="h-white">Erbverzichtsvertrag</text>
    <rect x="103" y="81" width="395" height="246" fill="var(--chart-bg)" role="img" aria-label="Eingefügte Grafik: Übersicht Erbteile und Pflichtteile für Alleinstehende und Ehepaare"/>
    <text x="590" y="358" text-anchor="end" class="brand">Tannquist Legal</text>
  </svg>
</div>

<!-- Erbverzichtsvertrag (Tabelle) -->
<div class="slide s8">
  <svg viewBox="0 0 600 364">
    <rect y="180" width="600" height="184" fill="var(--navy)"/>
    <rect y="184" width="600" height="4" fill="var(--white)"/>
    <text x="94" y="40" class="h">Erbverzichtsvertrag</text>
    <rect x="68" y="64" width="295" height="278" fill="#DADADA"/>
    <rect x="76" y="70" width="279" height="264" fill="#EFEFEF" role="img" aria-label="Eingefügte Tabelle: Erbteilung ohne Testament und Pflichtteile je nach Erbenkonstellation"/>
    <text x="583" y="358" text-anchor="end" class="brand-white">Tannquist Legal</text>
  </svg>
</div>

<!-- Gesetzliche Erbfolge und Pflichtteile -->
<div class="slide s9">
  <svg viewBox="0 0 600 364">
    <rect width="600" height="364" fill="var(--navy)"/>
    <polygon points="0,120 600,0 600,290 470,364 0,364" fill="var(--white)"/>
    <rect x="58" y="16" width="472" height="312" fill="#C8C8C8"/>
    <rect x="64" y="22" width="460" height="300" fill="#EDEDED" role="img" aria-label="Eingefügter Bildschirmausschnitt: Tabelle gesetzliche Erbfolge und Pflichtteile"/>
    <text x="590" y="358" text-anchor="end" class="brand-white">Tannquist Legal</text>
  </svg>
</div>

</body>
</html>
```